New business card design

I need original, modern, business looking but dzen (minimalistic) looking design.
Also refer to websit qvtrenda.ru

Text is

Зорин Виктор, PMP
Партнер

Моб. +7 (915) 460 1897
info@qvtrenda.ru
Москва, Россия, 117358, ул. Берёзовая 27/2
=====================

Zorin Viktor, PMP
Partner

Mob. +7 (915) 460 1897
info@qvtrenda.ru
Moscow, Russia,117358, Beryozovaya 27/2

```html
<!DOCTYPE html>
<html lang="en">
<head>
<meta charset="utf-8">
<title>Nordhaven business card</title>
<link href="https://fonts.googleapis.com/css2?family=Exo+2:wght@300&family=Michroma&display=swap" rel="stylesheet">
<style>
  :root {
    --bg: #e4e5e7;
    --card: #ffffff;
    --ink: #3b3d40;
    --ink-soft: #6b6e72;
    --accent: #2f86c9;
    --accent-light: #5cc4ea;
    --rule: #b9bcc0;
  }
  * { margin: 0; padding: 0; box-sizing: border-box; }
  html, body { width: 1200px; height: 771px; overflow: hidden; background: var(--bg); }
  .stage { position: relative; width: 1200px; height: 771px; }
  .card {
    position: absolute; top: 230px; width: 540px; height: 310px;
    background: var(--card); overflow: hidden;
    box-shadow: 0 10px 24px rgba(0,0,0,0.18);
  }
  .card--front { left: 40px; }
  .card--back { left: 620px; }

  .edge-band {
    position: absolute; left: 0; right: 0; bottom: 0; height: 12px;
    background: var(--accent);
  }
  .edge-band::before {
    content: ""; position: absolute; left: 0; right: 0; top: -5px; height: 2px;
    background: var(--accent-light);
  }

  .brand { position: absolute; display: flex; align-items: center; gap: 12px; }
  .brand__mark { background: var(--accent); }
  .brand__name {
    font-family: "Exo 2", sans-serif; font-weight: 300;
    color: var(--ink); letter-spacing: 0.5px; line-height: 1;
  }
  .card--front .brand { left: 50%; top: 50%; transform: translate(-50%, -50%); }
  .card--front .brand__mark { width: 44px; height: 44px; }
  .card--front .brand__name { font-size: 52px; }
  .card--back .brand { left: 50%; top: 40px; transform: translateX(-50%); }
  .card--back .brand__mark { width: 32px; height: 32px; }
  .card--back .brand__name { font-size: 38px; }

  .details {
    position: absolute; left: 0; right: 0; top: 128px;
    display: flex; justify-content: center; gap: 14px;
    font-family: "Michroma", sans-serif; font-size: 9px; line-height: 15px;
    color: var(--ink-soft); letter-spacing: 0.3px;
  }
  .identity { text-align: right; }
  .identity__name { color: var(--accent); font-size: 10px; text-transform: uppercase; }
  .identity__role { margin-bottom: 10px; }
  .divider { width: 1px; align-self: stretch; background: var(--rule); }
  .contacts { list-style: none; }
  .contacts li { display: flex; align-items: center; gap: 7px; margin-bottom: 4px; }
  .contacts svg { width: 11px; height: 11px; flex: none; }
</style>
</head>
<body>
<main class="stage">

  <section class="card card--front" aria-label="Card front">
    <div class="brand">
      <span class="brand__mark"></span>
      <span class="brand__name">Nordhaven</span>
    </div>
  </section>

  <section class="card card--back" aria-label="Card back">
    <div class="brand">
      <span class="brand__mark"></span>
      <span class="brand__name">Nordhaven</span>
    </div>

    <div class="details">
      <div class="identity">
        <p class="identity__name">Daniel Hart</p>
        <p class="identity__role">Owner / C.E.O</p>
        <p>Unit 14, Elm Court,</p>
        <p>OH 40127</p>
      </div>

      <span class="divider"></span>

      <ul class="contacts">
        <li>
          <svg viewBox="0 0 12 12"><circle cx="6" cy="6" r="6" fill="var(--accent)"/><path d="M4 3.2 L5 5 L4.4 5.6 Q5.4 7.2 6.6 7.8 L7.2 7.1 L8.9 8.1 L8.2 9 Q5 8.6 3.2 4 Z" fill="#fff"/></svg>
          <span>555-210-4481</span>
        </li>
        <li>
          <svg viewBox="0 0 12 12"><circle cx="6" cy="6" r="6" fill="var(--accent)"/><path d="M4 3.2 L5 5 L4.4 5.6 Q5.4 7.2 6.6 7.8 L7.2 7.1 L8.9 8.1 L8.2 9 Q5 8.6 3.2 4 Z" fill="#fff"/></svg>
          <span>555-318-2207</span>
        </li>
        <li>
          <svg viewBox="0 0 12 12"><circle cx="6" cy="6" r="6" fill="var(--accent)"/><path d="M4 3.2 L5 5 L4.4 5.6 Q5.4 7.2 6.6 7.8 L7.2 7.1 L8.9 8.1 L8.2 9 Q5 8.6 3.2 4 Z" fill="#fff"/></svg>
          <span>555-642-9035</span>
        </li>
        <li>
          <svg viewBox="0 0 12 12"><circle cx="6" cy="6" r="6" fill="var(--accent)"/><rect x="3" y="4" width="6" height="4.2" fill="none" stroke="#fff" stroke-width="0.9"/><path d="M3 4 L6 6.4 L9 4" fill="none" stroke="#fff" stroke-width="0.9"/></svg>
          <span>hello@nordhaven-pm.com</span>
        </li>
        <li>
          <svg viewBox="0 0 12 12"><circle cx="6" cy="6" r="6" fill="var(--accent)"/><circle cx="6" cy="6" r="3" fill="none" stroke="#fff" stroke-width="0.9"/><path d="M3 6 H9 M6 3 Q4.5 6 6 9 M6 3 Q7.5 6 6 9" fill="none" stroke="#fff" stroke-width="0.7"/></svg>
          <span>www.nordhaven-pm.com</span>
        </li>
      </ul>
    </div>

    <span class="edge-band"></span>
  </section>

</main>
</body>
</html>
```